Ferrando Quispe Law Firm for Small and Medium Business: Website

We need a web design that includes coding for the Wix platform, for a new company based in Santiago, Chile, called Ferrando Quispe, Abogados y Consultores. The company is essentially a law firm, with additional advisory services in accounting, tax management and finance. The main target of the company are founders, CEOs or C-level executives of small or medium companies based in Chile.
The main menu of the web page must have the following tab options:
- Home - About us - Services – How we work -Blog – FAQ -Contact
Our main services are:

1.- Commercial and corporate law advisory
2.- Legal defense in civil, criminal, labor and family matters (litigation and arbitration)
3.- Bankruptcy and reorganization of companies
4.- Collection and recovery of assets
5.- Asset protection
6.- Financial and tax advice

We want to highlight the following services:

-Bankruptcy and reorganization of companies
-Judicial defense in civil matters
-Financial and tax advice

In addition to these services, the following will be offered:
-Lawyer at your home for special cases
-Half hour free consultation
-Monthly service packages

The final design should communicate confidence, business savvy and high execution standards and quality.

Target Market(s)

The main target of the company are founders, CEOs or C-level executives of small or medium companies based in Chile.

Industry/Entity Type

Legal industry

Coding

Coded - Design and coding required

Number of Pages Required

5+ page

Font styles to use
Serif

Requirements
Must have
• 1. Big banners para destacar los siguientes servicios: -Bankruptcy and reorganization of companies -Judicial defense in civil matters -Financial and tax advice 2. Call to action para agendar consulta legal. 3. Destacar los siguientes servicios: -Lawyer at your home for special cases -Half hour free consultation -Monthly service packages 3. Página para explicar cómo se cobra (precios transparentes): ver el siguiente sitio web: https://www.brindlemoorlegal.example/how 4. Links to Facebook, Instagram and Linkedin 5. Connection to Whatsapp.
Should not have
• Look old fashioned

```html
<!DOCTYPE html>
<html lang="en">
<head>
<meta charset="utf-8">
<title>Ferrando Quispe, Abogados y Consultores</title>
<link rel="stylesheet" href="https://fonts.googleapis.com/css2?family=Playfair+Display:wght@400;700&family=Montserrat:wght@400;500;600;700&display=swap">
<style>
:root{
  --green-dark:#0f2e25;
  --green:#1b4a3c;
  --green-mid:#235a49;
  --gold:#c9ad4a;
  --gold-light:#e5d175;
  --gold-deep:#b3953a;
  --ink:#1f2a27;
  --body:#5b6662;
  --grey-bg:#eef1f5;
  --line:#d9dde0;
  --white:#ffffff;
}
*{margin:0;padding:0;box-sizing:border-box}
html,body{width:1200px;height:4431px;overflow:hidden}
body{position:relative;font-family:"Montserrat",sans-serif;color:var(--ink);background:var(--white)}
.abs{position:absolute}
.serif{font-family:"Playfair Display",serif}
a{color:inherit;text-decoration:none}

/* header */
.site-header{position:absolute;left:0;top:0;width:1200px;height:90px;background:var(--green-dark)}
.brand{position:absolute;left:103px;top:22px;display:flex;align-items:center;gap:12px}
.brand-mark{width:44px;height:44px;background:var(--gold)}
.brand-name{font-family:"Montserrat",sans-serif;font-size:30px;font-weight:400;color:var(--gold)}
.top-bar{position:absolute;top:8px;left:748px;display:flex;align-items:center;gap:14px}
.social-dot{width:20px;height:20px;border-radius:50%;background:var(--white);display:block}
.social-dot.chat{background:var(--gold-light);width:24px;height:24px}
.phone{display:flex;align-items:center;gap:5px;color:var(--white);font-weight:600;font-size:16px;margin-left:6px}
.main-nav{position:absolute;top:58px;left:495px;display:flex}
.main-nav a{font-size:12px;font-weight:600;color:var(--white);letter-spacing:.3px;margin-right:44px}
.main-nav a.active{color:var(--gold)}

/* hero */
.hero{position:absolute;left:0;top:90px;width:1200px;height:594px;background:linear-gradient(180deg,#1d4f40 0%,#1a4a3b 60%,#163f33 100%);overflow:hidden}
.hero-skyline{position:absolute;left:0;bottom:0;width:1200px;height:190px;background:linear-gradient(180deg,rgba(255,255,255,0) 0%,rgba(80,130,110,.25) 100%)}
.hero-frame{position:absolute;left:107px;top:125px;width:163px;height:297px;border:2px solid var(--white);border-right:none}
.hero-title{position:absolute;left:139px;top:158px;font-size:40px;line-height:43px;color:var(--white);font-weight:400}
.hero-title b{font-weight:700}
.hero-text{position:absolute;left:139px;top:292px;width:360px;font-size:12px;line-height:18px;color:#e2ebe7}
.btn-gold{display:inline-flex;align-items:center;justify-content:center;border-radius:24px;background:linear-gradient(90deg,var(--gold-light),var(--gold-deep));color:var(--white);font-weight:700;font-size:11px;letter-spacing:.4px}
.hero-cta{position:absolute;left:137px;top:345px;width:271px;height:45px;font-size:12px}
.hero-art{position:absolute;left:619px;top:39px;width:396px;height:396px;border-radius:50%;background:radial-gradient(circle at 50% 50%,#265d4c 0%,#18463a 70%,#143c31 100%)}
.hero-arrow{position:absolute;top:270px}

/* feature boxes */
.feature{position:absolute;text-align:center;color:var(--white)}
.feature h3{font-family:"Playfair Display",serif;font-weight:700;font-size:17px;line-height:19px}
.feature h3 span{font-weight:400;display:block}
.feature p{font-size:10px;line-height:15px;margin:10px auto 0;width:240px;color:rgba(255,255,255,.9)}
.feature .btn{display:inline-flex;align-items:center;justify-content:center;margin-top:16px;width:144px;height:30px;border-radius:16px;font-size:10px;font-weight:700}
.feature.gold{background:linear-gradient(90deg,var(--gold-deep),var(--gold-light));top:653px;height:186px;padding-top:37px}
.feature.gold .btn{background:var(--green-dark);color:var(--white)}
.feature.green{background:var(--green);top:615px;height:251px;padding-top:60px;left:413px;width:340px;box-shadow:0 10px 24px rgba(0,0,0,.2);z-index:2}
.feature.green h3{font-size:20px;line-height:24px}
.feature.green .btn{background:linear-gradient(90deg,var(--gold-light),var(--gold-deep));color:var(--white);width:122px}

/* about */
.about-art{position:absolute;left:89px;top:937px;width:464px;height:464px;border-radius:50%;background:radial-gradient(circle,#dde3e6 0%,#e9edef 60%,#f2f4f5 100%)}
.about-frame{position:absolute;left:889px;top:994px;width:188px;height:336px;border:2px solid var(--line);border-left:none}
.about-frame:before{content:"";position:absolute;left:0;top:0;width:2px;height:40px;background:var(--line)}
.about-frame:after{content:"";position:absolute;left:0;bottom:0;width:2px;height:40px;background:var(--line)}
.eyebrow{font-family:"Playfair Display",serif;letter-spacing:3px;font-size:14px;color:var(--gold)}
.about-eyebrow{position:absolute;left:609px;top:1017px}
.about-title{position:absolute;left:609px;top:1038px;font-size:32px;font-weight:400;color:var(--ink)}
.about-title b{font-weight:700}
.about-text{position:absolute;left:609px;top:1102px;width:440px;font-size:13px;line-height:26.5px;color:var(--body)}
.about-cta{position:absolute;left:609px;top:1275px;width:154px;height:40px}

/* services */
.services{position:absolute;left:0;top:1470px;width:1200px;height:779px;background:var(--grey-bg)}
.section-title{position:absolute;left:0;width:1200px;text-align:center;font-family:"Playfair Display",serif;font-size:38px;font-weight:400;color:var(--gold)}
.section-title b{color:var(--ink);font-weight:700}
.underline{position:absolute;left:565px;width:70px;height:3px;background:var(--gold)}
.card{position:absolute;width:315px;height:244px;background:var(--white);border:1px solid var(--line);padding:42px 0 0 33px}
.card.dark{background:linear-gradient(160deg,#1d5141,#0f2e25);border-color:transparent;box-shadow:0 18px 40px rgba(0,0,0,.25)}
.card h4{margin-top:20px;font-size:17px;font-weight:500;line-height:22px;color:var(--green-dark);width:290px;white-space:nowrap}
.card p{margin-top:14px;font-size:12.5px;line-height:22px;color:var(--body);width:265px}
.card.dark h4,.card.dark p{color:var(--white)}

/* charge */
.charge{position:absolute;left:0;top:2249px;width:1200px;height:713px;background:linear-gradient(180deg,#1c4c3d 0%,#123529 60%,#0e2c23 100%);overflow:hidden}
.charge .eyebrow{position:absolute;left:0;width:1200px;text-align:center;top:58px;color:#d6dcd9}
.charge-title{position:absolute;left:0;width:1200px;text-align:center;top:82px;font-size:34px;color:var(--white);font-weight:400}
.charge-title b{font-weight:700}
.step-num{position:absolute;width:70px;height:70px;border-radius:50%;background:radial-gradient(circle at 40% 35%,var(--gold-light),var(--gold-deep));color:var(--white);font-family:"Playfair Display",serif;font-size:30px;font-weight:700;display:flex;align-items:center;justify-content:center}
.step-label{position:absolute;font-size:12.5px;font-weight:700;color:var(--white);letter-spacing:.3px}
.step-text{position:absolute;width:280px;font-size:11px;line-height:18px;color:#b9c7c2}

/* blogs */
.blog-main{position:absolute;left:124px;top:3108px;width:485px;height:385px;background:linear-gradient(135deg,var(--gold-deep),var(--gold-light) 60%,var(--gold))}
.blog-main .art{position:absolute;left:60px;top:20px;width:360px;height:270px;border-radius:50%;background:rgba(255,255,255,.22)}
.date{display:inline-block;background:var(--green-dark);color:var(--white);font-size:11px;font-weight:600;padding:6px 10px}
.blog-main .date{position:absolute;left:40px;top:290px}
.blog-main h5{position:absolute;left:36px;top:326px;width:420px;font-size:18px;line-height:21px;font-weight:700;color:var(--green-dark)}
.blog-side{position:absolute;left:617px;width:449px;height:185px;background:var(--white);border:1px solid var(--line)}
.blog-side .thumb{position:absolute;left:0;top:0;width:217px;height:100%}
.blog-side .date{position:absolute;left:237px;top:33px;font-size:10px;padding:5px 10px}
.blog-side h6{position:absolute;left:239px;top:65px;font-size:12.5px;font-weight:700;color:var(--green-dark)}
.blog-side p{position:absolute;left:239px;top:87px;width:195px;font-size:11.5px;line-height:20px;color:var(--body)}

/* contact */
.contact{position:absolute;left:0;top:3590px;width:1200px;height:550px;background:linear-gradient(100deg,#e7d470 0%,#d6bf56 50%,#b89a3b 100%)}
.contact-title{position:absolute;left:139px;top:88px;font-size:34px;font-weight:400;color:var(--green-dark)}
.contact-title b{font-weight:700}
.field{position:absolute;background:var(--white);border:1px solid #e2e2e2;display:flex;align-items:center;gap:8px;padding-left:16px;font-size:10px;color:#555}
.field.area{align-items:flex-start;padding-top:14px}
.submit{position:absolute;left:141px;top:385px;width:182px;height:40px;background:var(--green-dark);color:var(--white);font-size:12px;font-weight:700;display:flex;align-items:center;justify-content:center;gap:6px}
.contact-art{position:absolute;left:627px;top:89px;width:460px;height:378px;border-radius:48% 52% 40% 60%;background:radial-gradient(circle at 50% 45%,#c8cfcc 0%,#a9b4b0 60%,#9aa59f 100%)}

/* footer */
.site-footer{position:absolute;left:0;top:4140px;width:1200px;height:291px;background:var(--green-dark);color:var(--white)}
.site-footer .brand{left:125px;top:70px}
.copy{position:absolute;left:125px;top:146px;font-size:10.5px;line-height:19px;color:#c4ccc9}
.copy span{color:var(--gold)}
.fdiv{position:absolute;top:62px;width:3px;height:18px;background:var(--white)}
.fcol h6{font-size:11.5px;font-weight:700;letter-spacing:.3px;margin-bottom:14px}
.fcol{position:absolute;top:63px;font-size:10.5px;line-height:21px;color:#dfe5e3}
.fsocial{display:flex;gap:12px;margin-top:2px}
.fsocial span{width:28px;height:28px;border-radius:50%;background:var(--gold);display:block}
</style>
</head>
<body>

<header class="site-header">
  <a class="brand" href="#"><span class="brand-mark"></span><span class="brand-name">Ferrando Quispe</span></a>
  <div class="top-bar">
    <a class="social-dot" href="#" aria-label="Social profile one"></a>
    <a class="social-dot" href="#" aria-label="Social profile two"></a>
    <a class="social-dot" href="#" aria-label="Social profile three"></a>
    <a class="social-dot chat" href="#" aria-label="Chat with us"></a>
    <span class="phone"><svg width="15" height="15" viewBox="0 0 24 24"><path fill="#fff" d="M6.6 10.8a15.1 15.1 0 0 0 6.6 6.6l2.2-2.2c.3-.3.7-.4 1-.2 1.1.4 2.3.6 3.6.6.6 0 1 .4 1 1V20c0 .6-.4 1-1 1A17 17 0 0 1 3 4c0-.6.4-1 1-1h3.5c.6 0 1 .4 1 1 0 1.3.2 2.5.6 3.6.1.3 0 .7-.2 1z"/></svg>(685) 555 0142</span>
  </div>
  <nav class="main-nav">
    <a class="active" href="#">ABOUT US</a>
    <a href="#">SERVICES</a>
    <a href="#">HOW WE WORK</a>
    <a href="#">BLOG</a>
    <a href="#">FAQ</a>
    <a href="#">CONTACT</a>
  </nav>
</header>

<section class="hero">
  <div class="hero-skyline" role="img" aria-label="Faint city skyline silhouette"></div>
  <div class="hero-frame"></div>
  <h1 class="hero-title serif"><b>BANKRUPTCY AND<br>REORGANIZATION</b><br>OF COMPANIES</h1>
  <p class="hero-text">Lorem Ipsum is simply dummy text of the printing and type-setting industry. Lorem Ipsum has been the</p>
  <a class="btn-gold hero-cta" href="#">SCHEDULE LEGAL CONSULTATION</a>
  <div class="hero-art" role="img" aria-label="Illustration of law books, gavel, scales and a signed contract"></div>
  <svg class="hero-arrow" style="left:24px" width="20" height="32" viewBox="0 0 20 32"><path d="M16 2 4 16l12 14" fill="none" stroke="#c9d3cf" stroke-width="3"/></svg>
  <svg class="hero-arrow" style="left:1146px" width="20" height="32" viewBox="0 0 20 32"><path d="M4 2l12 14L4 30" fill="none" stroke="#c9d3cf" stroke-width="3"/></svg>
</section>

<div class="feature gold" style="left:107px;width:306px">
  <h3>LAWYER AT YOUR HOME<span>FOR SPECIAL CASES</span></h3>
  <p>Lorem ipsum dolor sit amet, consectetur adipi-scing elit, sed do eiusmod tempo</p>
  <a class="btn" href="#">LEARN MORE</a>
</div>
<div class="feature green">
  <h3>HALF HOUR FREE<span>CONSULTATION</span></h3>
  <p>Lorem ipsum dolor sit amet, consectetur adipi-scing elit, sed do eiusmod tempor incididunt ut labore et dolore magna aliqua.</p>
  <a class="btn" href="#">LEARN MORE</a>
</div>
<div class="feature gold" style="left:753px;width:328px">
  <h3>MONTHLY SERVICE<span>PACKAGES</span></h3>
  <p>Lorem ipsum dolor sit amet, consectetur adipi-scing elit, sed do eiusmod tempor incididunt.</p>
  <a class="btn" href="#">LEARN MORE</a>
</div>

<section class="about">
  <div class="about-art" role="img" aria-label="Isometric illustration of a legal dashboard with scales and coins"></div>
  <div class="about-frame"></div>
  <p class="eyebrow about-eyebrow">WHO WE ARE</p>
  <h2 class="about-title serif">ABOUT <b>FERRANDO QUISPE</b></h2>
  <p class="about-text">Lorem Ipsum is simply dummy text of the printing and typeset-ting industry. Lorem Ipsum has been the industry's standard dummy text ever since the 1500s, when an unknown printer took a galley of type and scrambled it to make a type specimen book. It has survived not only five centuries.Lorem Ipsum is simply dummy text of the printing and typesetting industry</p>
  <a class="btn-gold about-cta" href="#">LEARN MORE</a>
</section>

<section class="services">
  <h2 class="section-title" style="top:58px">OUR <b>SERVICES</b></h2>
  <div class="underline" style="top:108px"></div>

  <div class="card" style="left:115px;top:160px">
    <svg width="50" height="46" viewBox="0 0 50 46" fill="none" stroke="#c9ad4a" stroke-width="2"><path d="M25 4v36M12 42h26M8 12h34M8 12 2 28h12zM42 12l-6 16h12z"/></svg>
    <h4>Commercial and<br>corporate law advisory</h4>
    <p>Lorem Ipsum is simply dummy text of the printing and typesetting industry.</p>
  </div>
  <div class="card dark" style="left:442px;top:160px">
    <svg width="54" height="46" viewBox="0 0 54 46" fill="none" stroke="#c9ad4a" stroke-width="2"><circle cx="17" cy="14" r="8"/><circle cx="37" cy="14" r="8"/><path d="M3 44c0-10 6-16 14-16s14 6 14 16M23 44c0-10 6-16 14-16s14 6 14 16"/></svg>
    <h4>Legal defense in civil, criminal,<br>labor and family matters</h4>
    <p>Lorem Ipsum is simply dummy text of the printing and typesetting industry.</p>
  </div>
  <div class="card" style="left:768px;top:160px">
    <svg width="52" height="46" viewBox="0 0 52 46" fill="none" stroke="#c9ad4a" stroke-width="2"><circle cx="12" cy="32" r="9"/><rect x="26" y="36" width="20" height="7"/><rect x="26" y="28" width="20" height="7"/><path d="M4 8l10 8 8-6 12 8"/><circle cx="42" cy="10" r="7"/></svg>
    <h4>Bankruptcy and<br>reorganization of companies</h4>
    <p>Lorem Ipsum is simply dummy text of the printing and typesetting industry.</p>
  </div>
  <div class="card" style="left:115px;top:412px">
    <svg width="52" height="46" viewBox="0 0 52 46" fill="none" stroke="#c9ad4a" stroke-width="2"><circle cx="24" cy="26" r="17"/><circle cx="24" cy="26" r="9"/><path d="M18 4h12M24 4v5M40 8l4-4"/></svg>
    <h4>Collection and<br>recovery of assets</h4>
    <p>Lorem Ipsum is simply dummy text of the printing and typesetting industry.</p>
  </div>
  <div class="card" style="left:442px;top:412px">
    <svg width="46" height="50" viewBox="0 0 46 50" fill="none" stroke="#c9ad4a" stroke-width="2"><path d="M23 3 5 10v14c0 12 8 20 18 23 10-3 18-11 18-23V10z"/><path d="M15 25l6 6 11-12"/></svg>
    <h4>Asset protection</h4>
    <p>Lorem Ipsum is simply dummy text of the printing and typesetting industry.</p>
  </div>
  <div class="card" style="left:768px;top:412px">
    <svg width="50" height="50" viewBox="0 0 50 50" fill="none" stroke="#c9ad4a" stroke-width="2"><rect x="6" y="4" width="30" height="40"/><path d="M12 14h18M12 22h18M14 30l14-8"/><circle cx="40" cy="40" r="6"/></svg>
    <h4>Financial and<br>tax advice</h4>
    <p>Lorem Ipsum is simply dummy text of the printing and typesetting industry.</p>
  </div>
</section>

<section class="charge">
  <p class="eyebrow">OUR PROCESS</p>
  <h2 class="charge-title serif">HOW WE <b>CHARGE</b></h2>
  <div class="underline" style="top:130px;background:var(--white)"></div>
  <svg class="abs" style="left:0;top:0" width="1200" height="713" viewBox="0 0 1200 713" fill="none" stroke="#b39a44" stroke-width="1.5">
    <path d="M228 220H820M890 220H1030a80 80 0 0 1 80 80v63a80 80 0 0 1-80 80H895M825 443H560M490 443H222"/>
    <path d="M336 212l8 8-8 8M330 220h14M706 212l8 8-8 8M700 220h14M376 435l8 8-8 8M370 443h14M711 435l8 8-8 8M705 443h14" stroke="#e5d175" stroke-width="2"/>
  </svg>
  <div class="step-num" style="left:158px;top:185px">1</div>
  <div class="step-num" style="left:482px;top:185px">2</div>
  <div class="step-num" style="left:819px;top:185px">3</div>
  <div class="step-num" style="left:152px;top:408px">4</div>
  <div class="step-num" style="left:489px;top:408px">5</div>
  <div class="step-num" style="left:825px;top:408px">6</div>

  <p class="step-label" style="left:158px;top:272px">PAY AS YOU GO</p>
  <p class="step-text" style="left:158px;top:294px">Lorem ipsum dolor sit amet co sec etur adipiscing elitLorem ipsum ec Lorem ipsum dolor sit amet co sec et</p>
  <p class="step-label" style="left:482px;top:272px">FIXED FEE</p>
  <p class="step-text" style="left:482px;top:294px">Lorem ipsum dolor sit amet co sec etur adipiscing elitLorem ipsum ec Lorem ipsum dolor sit amet co sec etur adipiscin</p>
  <p class="step-label" style="left:830px;top:272px">FIXED FEE</p>
  <p class="step-text" style="left:830px;top:294px">Lorem ipsum dolor sit amet co sec etur adipiscing elitLorem ipsum ec Lorem ipsum dolor sit amet co sec etur Lorem ipsum ec</p>
  <p class="step-label" style="left:151px;top:508px">CASE REVIEW</p>
  <p class="step-text" style="left:151px;top:530px">Lorem ipsum dolor sit amet co sec etur adipiscing elitLorem ipsum ec Lorem ipsum dolor sit amet co sec etur Lorem ipsum ec</p>
  <p class="step-label" style="left:487px;top:508px">INITIAL MEETING</p>
  <p class="step-text" style="left:487px;top:530px">Lorem ipsum dolor sit amet co sec etur adipiscing elitLorem ipsum ec Lorem ipsum dolor sit amet co sec etur Lorem ipsum ec</p>
  <p class="step-label" style="left:822px;top:508px">BEST OUTCOME FOR YOU</p>
  <p class="step-text" style="left:822px;top:530px">Lorem ipsum dolor sit amet co sec etur adipiscing elitLorem ipsum ec Lorem ipsum dolor sit amet co sec etur Lorem ipsum ec</p>
</section>

<section class="blogs">
  <h2 class="section-title" style="top:3006px">LATEST <b>BLOGS</b></h2>
  <div class="underline" style="top:3058px"></div>

  <article class="blog-main">
    <div class="art" role="img" aria-label="Illustration of two professionals meeting at a round table"></div>
    <span class="date">28 MAY 2021</span>
    <h5>Lorem ipsum dolor sit amet, consectetur ad-ipiscing elit, sed do eiusmod tempor</h5>
  </article>

  <article class="blog-side" style="top:3108px">
    <div class="thumb" role="img" aria-label="Illustration of a lawyer beside scales of justice" style="background:linear-gradient(135deg,#eef0ee,#1d4a3c)"></div>
    <span class="date">19 MAY 2021</span>
    <h6>Lorem ipsum dolor sit</h6>
    <p>Duis aute irure dolor in repre-henderit in voluptate velit esse cillum dolore eu fugiat</p>
  </article>
  <article class="blog-side" style="top:3306px">
    <div class="thumb" role="img" aria-label="Illustration of analysts working with charts" style="background:linear-gradient(135deg,#2b2f33,#444a50)"></div>
    <span class="date">18 MAY 2021</span>
    <h6>Lorem ipsum dolor sit</h6>
    <p>Duis aute irure dolor in repre-henderit in voluptate velit esse cillum dolore eu fugiat</p>
  </article>
</section>

<section class="contact">
  <h2 class="contact-title serif">LEAVE US A <b>MESSAGE</b></h2>
  <div class="field" style="left:138px;top:172px;width:227px;height:38px"><svg width="11" height="11" viewBox="0 0 12 12"><circle cx="6" cy="3.5" r="3" fill="#333"/><path d="M0 12c0-4 3-5.5 6-5.5s6 1.5 6 5.5z" fill="#333"/></svg>First Name</div>
  <div class="field" style="left:375px;top:172px;width:227px;height:38px"><svg width="12" height="10" viewBox="0 0 12 10"><rect width="12" height="10" fill="#333"/><path d="M0 0l6 5 6-5" stroke="#fff" fill="none"/></svg>E-mail</div>
  <div class="field" style="left:138px;top:220px;width:227px;height:38px"><svg width="11" height="11" viewBox="0 0 12 12"><circle cx="6" cy="3.5" r="3" fill="#333"/><path d="M0 12c0-4 3-5.5 6-5.5s6 1.5 6 5.5z" fill="#333"/></svg>Last Name</div>
  <div class="field" style="left:375px;top:220px;width:227px;height:38px"><svg width="11" height="11" viewBox="0 0 24 24"><path fill="#333" d="M6.6 10.8a15.1 15.1 0 0 0 6.6 6.6l2.2-2.2c.3-.3.7-.4 1-.2 1.1.4 2.3.6 3.6.6.6 0 1 .4 1 1V20c0 .6-.4 1-1 1A17 17 0 0 1 3 4c0-.6.4-1 1-1h3.5c.6 0 1 .4 1 1 0 1.3.2 2.5.6 3.6.1.3 0 .7-.2 1z"/></svg>Phone</div>
  <div class="field area" style="left:138px;top:268px;width:464px;height:97px">Leave Message</div>
  <a class="submit" href="#">SUBMIT MESSAGE <svg width="12" height="12" viewBox="0 0 12 12"><path d="M0 6 12 0 9 12 6 8z" fill="#fff"/></svg></a>
  <div class="contact-art" role="img" aria-label="Illustration of hands typing on a laptop beside a notepad"></div>
</section>

<footer class="site-footer">
  <a class="brand" href="#"><span class="brand-mark"></span><span class="brand-name">Ferrando Quispe</span></a>
  <p class="copy">Copyright 2021Ferrando Quispe .All Right Reserved<br><span>Privacy Policy</span> | <span>Terms &amp; Condition</span></p>
  <span class="fdiv" style="left:459px"></span>
  <span class="fdiv" style="left:718px"></span>
  <span class="fdiv" style="left:905px"></span>
  <div class="fcol" style="left:504px">
    <h6>CONTACT US</h6>
    2210 Alameda Norte<br>Santiago, RM 8320000<br>Tel: (1300) 555 0142<br>Email: info@ferrandoquispe.example
  </div>
  <div class="fcol" style="left:756px">
    <h6>NAVIGATE</h6>
    About us<br>Services<br>How we work<br>Blog<br>FAQ<br>Contact
  </div>
  <div class="fcol" style="left:947px">
    <h6>FOLLOW US</h6>
    <div class="fsocial"><a href="#" aria-label="Social profile one"><span></span></a><a href="#" aria-label="Social profile two"><span></span></a><a href="#" aria-label="Social profile three"><span></span></a></div>
  </div>
</footer>

</body>
</html>
```